Social Media Marketing company needs a logo (tweak) and business card design

We need to slightly tidy up our logo, mainly to make sure we have the right design file (AI file type) also if possible remove the text below, for the business card we would like to get a fun yet professional feeling since we focus on social media marketing as well as event management
Target Market(s)
All industry really, just trying to look fun and professional to every one.
Industry/Entity Type
Marketing
Contact Information for Business Card
The Business Card needed to be fun yet professional
Font styles to use
Sans Serif
Colors
85cae6
Requirements
Must have
- The Logo.
- On the Name area, please provide two spaces 1. for English and Chinese.
- Rest is English only.
- Do not include a post code space.
- Phone number.
- Also please add website address www.brellavo.com
Nice to have
- Some water marks would be nice.
- Also the slogan "bright moves every day"

```html
<!DOCTYPE html>
<html lang="en">
<head>
<meta charset="utf-8">
<title>Brellavo Business Card</title>
<link rel="stylesheet" href="https://fonts.googleapis.com/css2?family=Comfortaa:wght@400;500&family=Noto+Sans+SC:wght@400&display=swap">
<style>
  :root {
    --stage: #e9ebec;
    --card-dark: #3a3a3c;
    --brand-blue: #85cae6;
    --mark-faint: #4a4a4d;
    --line-dark: #333335;
  }
  * { box-sizing: border-box; margin: 0; padding: 0; }
  html, body { width: 1200px; height: 900px; overflow: hidden; }
  body {
    background: var(--stage);
    font-family: "Comfortaa", "Quicksand", sans-serif;
    display: flex;
    align-items: center;
    justify-content: center;
    gap: 48px;
  }
  .card {
    position: relative;
    width: 520px;
    height: 297px;
    background: var(--card-dark);
    overflow: hidden;
    box-shadow: 0 6px 18px rgba(0,0,0,0.18);
  }

  /* Front */
  .watermark {
    position: absolute;
    border-radius: 40px;
    background: radial-gradient(circle at 50% 50%, var(--mark-faint), var(--card-dark) 72%);
  }
  .watermark--upper { right: 30px; top: -10px; width: 210px; height: 150px; }
  .watermark--lower { left: 20px; bottom: -20px; width: 230px; height: 170px; }
  .brand {
    position: absolute;
    left: 70px;
    top: 112px;
    color: var(--brand-blue);
  }
  .brand__name {
    font-size: 58px;
    font-weight: 500;
    letter-spacing: 0.5px;
    line-height: 1;
  }
  .brand__slogan {
    margin-top: 8px;
    margin-left: 112px;
    font-size: 14px;
    letter-spacing: 0.8px;
  }

  /* Back */
  .back__art { position: absolute; inset: 0; }
  .tree-placeholder {
    position: absolute;
    left: 30px;
    top: 130px;
    width: 160px;
    height: 140px;
    border-radius: 50% 50% 12px 12px;
    background: radial-gradient(circle at 50% 40%, #5f8fa3, var(--brand-blue) 75%);
  }
  .person {
    position: absolute;
    left: 300px;
    top: 34px;
    color: var(--brand-blue);
    line-height: 1.2;
  }
  .person__name { font-size: 26px; font-weight: 500; }
  .person__name-cn {
    font-family: "Noto Sans SC", sans-serif;
    font-size: 20px;
    margin-top: 2px;
  }
  .contact {
    position: absolute;
    color: var(--brand-blue);
    font-size: 13px;
    letter-spacing: 0.3px;
    line-height: 1;
    white-space: nowrap;
  }
  .contact--web { left: 300px; top: 102px; }
  .contact--phone { left: 264px; top: 144px; }
  .contact--email { left: 322px; top: 189px; }
</style>
</head>
<body>
  <section class="card card--front" aria-label="Card front">
    <div class="watermark watermark--upper" role="img" aria-label="Faint circuit-tree watermark"></div>
    <div class="watermark watermark--lower" role="img" aria-label="Faint circuit-tree watermark"></div>
    <div class="brand">
      <div class="brand__name">Brellavo</div>
      <div class="brand__slogan">bright moves every day</div>
    </div>
  </section>

  <section class="card card--back" aria-label="Card back">
    <svg class="back__art" width="520" height="297" viewBox="0 0 520 297" aria-hidden="true">
      <polygon points="0,0 40,0 430,297 0,297" fill="#85cae6"/>
      <line x1="40" y1="0" x2="430" y2="297" stroke="#333335" stroke-width="3"/>
      <line x1="28" y1="0" x2="418" y2="297" stroke="#333335" stroke-width="2"/>
      <!-- phone badge -->
      <circle cx="237" cy="150" r="16" fill="#3a3a3c" stroke="#333335" stroke-width="3"/>
      <path d="M229 154 q8 -10 16 0 v4 h-16 z" fill="#85cae6"/>
      <rect x="227" y="142" width="20" height="5" rx="2.5" fill="#85cae6"/>
      <!-- email badge -->
      <circle cx="296" cy="195" r="16" fill="#3a3a3c" stroke="#333335" stroke-width="3"/>
      <rect x="286" y="188" width="20" height="14" fill="#85cae6"/>
      <polyline points="286,188 296,196 306,188" fill="none" stroke="#3a3a3c" stroke-width="1.5"/>
    </svg>
    <div class="tree-placeholder" role="img" aria-label="Circuit-board tree illustration"></div>
    <div class="person">
      <div class="person__name">Alex Moran</div>
      <div class="person__name-cn" lang="zh">王明</div>
    </div>
    <div class="contact contact--web">www.brellavo.com</div>
    <div class="contact contact--phone">555 210 3874</div>
    <div class="contact contact--email">hello@brellavo.com</div>
  </section>
</body>
</html>
```